Dr K.L. Fenwick, Consultant General Surgeon

Modern minimalistic look [shades of blue should be included]
I would like an interactive website which gives information about
1. Home page: office location
Medical Partners
📞(555) 555-0192-7
📱(876) 555-0147
📍42 Marigold Crescent, Kingston 10

VelaMedix
1-876-555-0163 / 1-876-555-0178 / 1-876-555-0129
📍37 North Cedar Grove RD, Kingston, Jamaica (Upstairs Brisa Linwood)
Info@velamedix.example

Beacon Care Medical Suites
📞(876) 555-0184
📱(876) 555-0136
📍Shop 22-23, Palm Crest Shopping Mall, Brookhaven

Corwell Medical Centre
📞 (876) 555-0151
📍 9 Pellowin Street , May Pen
The office logos will be attached
Booking details on this page or 2nd page with procedures

2. My surgical services . - I will attach a business card with the information for this section - do not upload the actual business card on the site

3. Allow the booking of appointments at any of the offices
4. A section where short explainer videos will be uploaded (this section is titled "Surgery in 3D"- I will upload an example below
5. A section- which shows videos of procedures. This section is titled "Surgical procedures" - I will upload one below
these videos will similar the same as the ones on my Instagram account
Link: https://www.instagram.com/dr_klfenwick?igsh=QmVyZXhhbXBsZQ&utm_source=qr

6. Gallery- section with pictures from interviews/ presentations/conferences etc

Each section should be on a different page.
The clearly defined sections can be represented from a HOME PAGE or drop-down menu
SIMILAR websites:
Modern professional design style (fonts and layout)- https://brightscalpelstudio.example
others -- this best captures the style I'm looking for. I prefer if the page is not crowded
https://velamedix.example
layered effect -- https://quillbankclinic.example/general-surgeon/
https://drpetrahalvik.example

I have updated the brief

Target Market(s)

Patients who require general surgical care

Coding

Coded - Design and coding required

Number of Pages Required

5+ page

Requirements
Must have
• Each section should be on a different page.

```html
<!DOCTYPE html>
<html lang="en">
<head>
<meta charset="utf-8">
<title>Dr K.L. Fenwick — Consultant General Surgeon</title>
<link rel="stylesheet" href="https://fonts.googleapis.com/css2?family=Montserrat:wght@500;600;700;800&family=Lato:wght@400;700&display=swap">
<style>
:root{
  --navy:#2b2f55;
  --navy-dark:#1f2344;
  --teal:#2d92b4;
  --card-navy:#363a5e;
  --sky:#e3f3fb;
  --blue:#0a68b8;
  --blue-light:#1483d2;
  --red:#e01e26;
  --footer:#1d1d1f;
  --text:#2c2c34;
  --white:#ffffff;
}
*{box-sizing:border-box;margin:0;padding:0}
html,body{width:1200px;height:4024px;overflow:hidden}
body{position:relative;background:var(--white);font-family:'Lato',sans-serif;color:var(--text)}
.abs{position:absolute}
h1,h2,h3,.heading{font-family:'Montserrat',sans-serif}
.underline{position:absolute;height:3px;width:72px;border-radius:2px;background:linear-gradient(90deg,var(--navy),var(--teal))}

/* header */
.brand{position:absolute;display:flex;align-items:center;gap:10px}
.brand-mark{width:38px;height:38px;border-radius:50%;border:3px solid var(--navy)}
.brand-name{font-family:'Montserrat',sans-serif;font-weight:800;font-size:21px;color:var(--navy);letter-spacing:.3px;white-space:nowrap}
.nav{position:absolute;top:38px;font-family:'Montserrat',sans-serif;font-size:14px;font-weight:500;color:var(--text);white-space:nowrap}
.nav.active{font-weight:700;color:var(--navy)}
.btn{position:absolute;display:flex;align-items:center;justify-content:center;border-radius:22px;font-family:'Montserrat',sans-serif;font-weight:700;font-size:13px;letter-spacing:.2px;white-space:nowrap}
.btn-navy{background:linear-gradient(90deg,var(--navy),var(--teal));color:var(--white)}

/* hero */
.hero{left:28px;top:97px;width:1152px;height:514px;background:var(--sky)}
.hero-title{left:110px;top:222px;font-size:56px;font-weight:800;color:var(--navy-dark);letter-spacing:-.5px;white-space:nowrap}
.hero-sub{left:110px;top:302px;font-size:18px;font-weight:500;color:var(--navy)}
.hero-text{left:110px;top:357px;width:410px;font-size:15px;line-height:27px}
.hero-photo{left:690px;top:139px;width:400px;height:400px;border-radius:50%;background:radial-gradient(circle at 40% 45%,#3aa58a,#1e7a64 60%,#5f8d72)}
.vertical-name{left:1122px;top:605px;width:505px;height:66px;transform-origin:0 0;transform:rotate(-90deg);font-family:'Montserrat',sans-serif;font-weight:800;font-size:55px;line-height:66px;color:var(--white);opacity:.9;white-space:nowrap;text-align:left}
.play{position:absolute;border-radius:50%;background:var(--red);box-shadow:0 0 0 10px rgba(224,30,38,.35)}

/* about */
.photo{position:absolute;border-radius:10px}
.section-title{position:absolute;font-size:36px;font-weight:800;color:var(--navy-dark);letter-spacing:.5px;white-space:nowrap}
.about-text{left:600px;top:750px;width:490px;font-size:14.5px;line-height:25.5px}
.about-text p+p{margin-top:26px}

/* videos */
.video-band{left:0;top:1311px;width:1200px;height:397px;background:linear-gradient(100deg,#5f7f9e,#40607d 40%,#7899b4 70%,#50657c)}
.services-bg{left:0;top:1708px;width:1200px;height:650px;background:var(--sky)}
.card{position:absolute;width:301px;height:393px;border-radius:6px}
.card-teal{background:var(--teal)}
.card-navy{background:var(--card-navy);box-shadow:0 8px 18px rgba(0,0,0,.25)}
.card-img{position:absolute;left:31px;top:-30px;width:270px;height:240px;border-radius:6px 6px 0 0}
.card-body{position:absolute;left:31px;top:232px;width:250px;color:var(--white)}
.card-body h3{font-size:17px;font-weight:600}
.card-body p{font-size:12.5px;line-height:23px;margin-top:8px;opacity:.9}
.card-body a{display:block;font-size:13px;font-weight:700;text-decoration:underline;margin-top:12px;margin-left:4px;color:var(--white)}
.arrow{position:absolute;width:34px;height:34px}

.video-3d{left:110px;top:2532px;width:978px;height:503px;border-radius:36px;border:3px solid var(--white);background:linear-gradient(100deg,#4e7394,#6c8fae 35%,#3d5876 60%,#8aa9c4);box-shadow:0 4px 14px rgba(0,0,0,.1)}
.quote{left:0;top:2847px;width:1200px;height:613px;background:linear-gradient(120deg,var(--blue) 0%,#0a5faa 50%,var(--blue-light) 100%)}
.quote-title{left:0;top:3098px;width:1200px;text-align:center;font-size:36px;font-weight:800;color:var(--white);letter-spacing:.3px}
.quote-text{left:170px;width:860px;text-align:center;color:var(--white);font-size:15px;line-height:27px}
.btn-white{background:var(--white);color:var(--navy)}
.btn-outline{border:2px solid var(--white);color:var(--white)}

/* footer */
.footer{left:0;top:3460px;width:1200px;height:564px;background:var(--footer)}
.field{position:absolute;top:3537px;width:184px;height:50px;border-radius:25px;background:var(--white);font-family:'Montserrat',sans-serif;font-weight:600;font-size:14px;color:var(--navy-dark);padding:16px 0 0 20px}
.submit{position:absolute;left:907px;top:3537px;width:184px;height:50px;border-radius:25px;background:linear-gradient(90deg,var(--navy),var(--teal));color:var(--white);font-family:'Montserrat',sans-serif;font-weight:700;font-size:17px;display:flex;align-items:center;justify-content:center}
.rule{position:absolute;left:111px;width:980px;height:1px;background:#3b3b40}
.foot-logo{left:111px;top:3700px;width:294px;height:118px;background:var(--white);border-radius:4px}
.foot-col h4{font-family:'Montserrat',sans-serif;font-weight:700;font-size:18px;color:var(--white);margin-bottom:14px;white-space:nowrap}
.foot-col li{list-style:none;font-size:14.5px;color:#e9e9ee;height:34.5px;white-space:nowrap}
.contact-item{position:absolute;left:867px;display:flex;gap:13px;color:#e9e9ee;font-size:14.5px;line-height:27px}
.icon{width:32px;height:32px;border-radius:50%;background:#2f5f9c;flex:none;display:flex;align-items:center;justify-content:center}
.copy{left:0;top:3975px;width:1200px;text-align:center;color:var(--white);font-size:14px}
</style>
</head>
<body>

<!-- Header -->
<div class="brand" style="left:110px;top:25px">
  <span class="brand-mark"></span>
  <span class="brand-name">DR. K.L. FENWICK</span>
</div>
<span class="nav active" style="left:437px">HOME</span>
<span class="nav" style="left:533px">ABOUT</span>
<span class="nav" style="left:635px">SERVICES <svg width="10" height="8" viewBox="0 0 10 8"><path d="M2 2l3 3 3-3" fill="none" stroke="#2c2c34" stroke-width="1.3"/></svg></span>
<span class="nav" style="left:756px">SURGICAL PROCEDURES</span>
<span class="btn btn-navy" style="left:969px;top:28px;width:120px;height:39px;font-size:12.5px">CONTACT US</span>

<!-- Hero -->
<div class="abs hero"></div>
<div class="abs vertical-name">DR.K.L.FENWICK</div>
<h1 class="abs hero-title">DR. K.L.FENWICK</h1>
<div class="abs hero-sub heading">CONSULTANT GENERAL SURGEON</div>
<span class="underline" style="left:112px;top:335px"></span>
<p class="abs hero-text">Lorem ipsum dolor sit amet, consectetur adipiscing elit, sed do eiusmod tempor incididunt ut labore et dolore magna aliqua.</p>
<span class="btn btn-navy" style="left:110px;top:456px;width:221px;height:42px">BOOK AN APPOINTMENT</span>
<svg class="abs" style="left:645px;top:445px" width="140" height="140" viewBox="0 0 140 140">
  <defs><pattern id="dotgrid" width="12" height="12" patternUnits="userSpaceOnUse"><circle cx="3" cy="3" r="1.8" fill="#2b2f55"/></pattern></defs>
  <rect x="0" y="0" width="36" height="140" fill="url(#dotgrid)"/>
  <rect x="0" y="104" width="140" height="36" fill="url(#dotgrid)"/>
</svg>
<div class="abs hero-photo" role="img" aria-label="Surgeon in green scrubs and cap operating"></div>
<div class="play" style="left:855px;top:295px;width:100px;height:100px"></div>
<svg class="abs" style="left:888px;top:328px" width="36" height="36" viewBox="0 0 36 36"><path d="M6 3l26 15L6 33z" fill="#fff"/></svg>

<!-- About -->
<svg class="abs" style="left:65px;top:1012px" width="140" height="140" viewBox="0 0 140 140">
  <rect x="0" y="0" width="36" height="140" fill="url(#dotgrid)"/>
  <rect x="0" y="104" width="140" height="36" fill="url(#dotgrid)"/>
</svg>
<div class="photo" style="left:110px;top:700px;width:205px;height:408px;background:linear-gradient(180deg,#d9c58a,#e9e4d2 30%,#3a3d48 60%,#d2b54b)" role="img" aria-label="Portrait of the surgeon in a dark suit at a conference banner"></div>
<div class="photo" style="left:320px;top:700px;width:204px;height:290px;background:linear-gradient(160deg,#7d95a6,#3f8f79 55%,#2c6f5d)" role="img" aria-label="Surgeon operating in theatre"></div>
<div class="photo" style="left:320px;top:997px;width:204px;height:111px;background:linear-gradient(110deg,#a6b6c4,#5a7fa8 60%,#354a66)" role="img" aria-label="Surgical team at a laparoscopy screen"></div>
<h2 class="section-title" style="left:600px;top:688px">ABOUT <span>DR.K.L.FENWICK</span></h2>
<div class="abs about-text">
  <p>Lorem ipsum dolor sit amet, consectetur adipiscing elit, sed do eiusmod incididunt ut labore et dolore magna aliqua. Ut enim ullamco laboris nisi aliquip ex ea commodoad minim venm, quis nostrud exercitation ullmco laboris nisi ut aliquip ex ea commodo consequat.</p>
  <p>Duis aute irure dolor in reprehenderit in voluptate velit esse cillum sunt culpa qui officia deserunt mollit anim id est laborum doloe eu fugiat nulla pariatur. Excepteur sint occaecat cupidatat non proident, sunt in culpa qui officia deserunt mollit anim id est laborum. Ut enim ad minim veniam, quis nostrud exercitation ullamco laboris nisi ut aliquip ex ea commodo consequat. Duis aute irure dolor in reprehenderit in voluptate velit esse cillum dolore eu fugiat nulla pariatur.</p>
</div>
<span class="btn btn-navy" style="left:600px;top:1073px;width:127px;height:40px">READ MORE</span>

<!-- Surgical procedures -->
<h2 class="section-title" style="left:0;width:1200px;text-align:center;top:1212px">SURGICAL PROCEDURES</h2>
<span class="underline" style="left:564px;top:1267px"></span>
<div class="abs video-band" role="img" aria-label="Video still of a surgical team performing a laparoscopic procedure"></div>
<div class="play" style="left:550px;top:1473px;width:100px;height:100px"></div>
<svg class="abs" style="left:583px;top:1506px" width="36" height="36" viewBox="0 0 36 36"><path d="M6 3l26 15L6 33z" fill="#fff"/></svg>

<!-- Services -->
<div class="abs services-bg"></div>
<h2 class="section-title" style="left:0;width:1200px;text-align:center;top:1772px">OUR SERVICES</h2>
<span class="underline" style="left:564px;top:1826px"></span>

<svg class="arrow" style="left:34px;top:2055px" viewBox="0 0 34 34"><circle cx="17" cy="17" r="16" fill="none" stroke="#2c2c34" stroke-width="1.5"/><path d="M24 17H10M15 12l-5 5 5 5" fill="none" stroke="#2c2c34" stroke-width="1.5"/></svg>
<svg class="arrow" style="left:1136px;top:2055px" viewBox="0 0 34 34"><circle cx="17" cy="17" r="16" fill="none" stroke="#2c2c34" stroke-width="1.5"/><path d="M10 17h14M19 12l5 5-5 5" fill="none" stroke="#2c2c34" stroke-width="1.5"/></svg>

<svg class="abs" style="left:694px;top:2218px" width="92" height="88" viewBox="0 0 92 88">
  <rect x="56" y="0" width="36" height="88" fill="url(#dotgrid)"/>
  <rect x="0" y="52" width="92" height="36" fill="url(#dotgrid)"/>
</svg>

<div class="card card-teal" style="left:125px;top:1905px">
  <div class="card-img" style="background:linear-gradient(180deg,#c98a5e,#b35a2e 50%,#7c5a4a)" role="img" aria-label="Illustration of the abdomen showing the intestines"></div>
  <div class="card-body"><h3>Hernia repair</h3><p>Excepteur sint occaecat cupidatat non i llit anim id est laborum.</p><a>Read More</a></div>
</div>
<div class="card card-navy" style="left:465px;top:1905px">
  <div class="card-img" style="background:linear-gradient(180deg,#d6d6da,#efefef 50%,#c9b5aa)" role="img" aria-label="Hands over chest with a pink awareness ribbon"></div>
  <div class="card-body"><h3>Breast cancer surgery</h3><p>Excepteur sint occaecat cupidatat non i llit anim id est laborum.</p><a>Read More</a></div>
</div>
<div class="card card-teal" style="left:803px;top:1905px">
  <div class="card-img" style="background:radial-gradient(circle at 50% 60%,#e59a4a,#2f4f86 45%,#16254a)" role="img" aria-label="Glowing illustration of the digestive tract and appendix"></div>
  <div class="card-body"><h3>Appendix</h3><p>Excepteur sint occaecat cupidatat non i llit anim id est laborum.</p><a>Read More</a></div>
</div>

<!-- Surgery in 3D -->
<h2 class="section-title" style="left:0;width:1200px;text-align:center;top:2419px">SURGERY IN 3D</h2>
<span class="underline" style="left:564px;top:2474px"></span>
<div class="abs quote"></div>
<div class="abs video-3d" role="img" aria-label="Video still of surgeons operating with laparoscopic instruments"></div>
<div class="play" style="left:550px;top:2733px;width:100px;height:100px"></div>
<svg class="abs" style="left:583px;top:2766px" width="36" height="36" viewBox="0 0 36 36"><path d="M6 3l26 15L6 33z" fill="#fff"/></svg>

<h2 class="abs quote-title">GET A FREE QUOTE AND CONSULTATION</h2>
<span class="underline" style="left:564px;top:3152px;background:var(--white)"></span>
<p class="abs quote-text" style="top:3181px">Lorem ipsum dolor sit amet, consectetur adipiscing elit, sed do eiusmod tempor incididunt ut labore et dolore magna aliqua. Ut enim ad minim veniam, quis nostrud exercitation ullamco laboris nisi ut aliquip ex ea commodo consequat.</p>
<p class="abs quote-text" style="top:3262px">Duis aute irure dolor in reprehenderit in voluptate velit esse cillum dolore eu fugiat nulla pariatur. Excepteur sint occaecat cupidatat non proident, sunt in culpa qui officia deserunt mollit anim id est laborum.</p>
<span class="btn btn-white" style="left:408px;top:3342px;width:127px;height:40px">CONTACT US</span>
<span class="btn btn-outline" style="left:562px;top:3342px;width:230px;height:40px">CALL US: +1 888 888 8888</span>

<!-- Footer -->
<div class="abs footer"></div>
<div class="field" style="left:115px">Name</div>
<div class="field" style="left:313px">Email</div>
<div class="field" style="left:511px">Phone Number</div>
<div class="field" style="left:709px">Address</div>
<div class="submit">SUBMIT</div>
<div class="rule" style="top:3645px"></div>

<div class="abs foot-logo"></div>
<div class="brand" style="left:137px;top:3741px">
  <span class="brand-mark"></span>
  <span class="brand-name">DR. K.L. FENWICK</span>
</div>

<div class="abs foot-col" style="left:457px;top:3692px">
  <h4>QUICK LINKS</h4>
  <ul><li>Home</li><li>About</li><li>Services</li><li>Surgical Procedures</li><li>Contact Us</li></ul>
</div>
<div class="abs foot-col" style="left:678px;top:3692px">
  <h4>HELP LINKS</h4>
  <ul><li>FAQ</li><li>Terms of use</li><li>Privacy Policy</li><li>Support Links</li><li>Legal Notices</li></ul>
</div>
<div class="abs foot-col" style="left:867px;top:3692px"><h4>CONTACT US</h4></div>
<div class="contact-item" style="top:3735px">
  <span class="icon"><svg width="14" height="18" viewBox="0 0 14 18"><path d="M7 1a6 6 0 0 0-6 6c0 4.5 6 10 6 10s6-5.5 6-10a6 6 0 0 0-6-6z" fill="#fff"/><circle cx="7" cy="7" r="2.2" fill="#2f5f9c"/></svg></span>
  <span>Shop 22-23, Palm Crest<br>Shopping Mall, Brookhaven</span>
</div>
<div class="contact-item" style="top:3803px">
  <span class="icon"><svg width="16" height="16" viewBox="0 0 16 16"><path d="M4 1l3 3-1.6 2a9 9 0 0 0 4.6 4.6L12 9l3 3-2 2.5C7 14 2 9 1.5 3z" fill="#fff"/></svg></span>
  <span>(555) 555-0192-7</span>
</div>
<div class="contact-item" style="top:3855px">
  <span class="icon"><svg width="16" height="12" viewBox="0 0 16 12"><rect x="0.5" y="0.5" width="15" height="11" rx="1.5" fill="#fff"/><path d="M1 1.5l7 5 7-5" fill="none" stroke="#2f5f9c" stroke-width="1.3"/></svg></span>
  <span>klf.surgeon@example.com</span>
</div>
<div class="rule" style="top:3945px"></div>
<p class="abs copy">Copyrights@2024.Dr.K.L.Fenwick.All Rights Reserved</p>

</body>
</html>
```